quiet orchard

It is a small business that is looking to sell medical supplies and services. later down the line it will branch off to help solve other world problems, i.e. global warming and raw material shortages.
but we will start with hospital equipment and supplies.

Target Market(s)

all medical facilities

Coding

Coded - Design and coding required

Number of Pages Required

1 page

```html
<!DOCTYPE html>
<html lang="en">
<head>
<meta charset="utf-8">
<title>Quiet Orchard</title>
<link href="https://fonts.googleapis.com/css2?family=Mulish:wght@300;400;600;800&display=swap" rel="stylesheet">
<style>
:root{
  --ink:#333333;
  --text:#3d3d3d;
  --muted:#b3b3b3;
  --line:#cfcfcf;
  --button:#c4c4c4;
  --white:#ffffff;
  --hero-top:#8c9198;
  --hero-mid:#9aa3ab;
  --footer:#2d3a4a;
}
*{margin:0;padding:0;box-sizing:border-box}
html,body{width:1200px;height:3778px;overflow:hidden;background:var(--white)}
body{position:relative;font-family:"Mulish",sans-serif;color:var(--text);letter-spacing:1px}
.abs{position:absolute}

/* hero */
.hero{left:0;top:0;width:1200px;height:755px;
  background:linear-gradient(180deg,var(--hero-top) 0%,var(--hero-mid) 35%,#8fa6b8 60%,#a8b6c2 82%,var(--white) 100%)}
.hero-tubes{left:0;top:220px;width:1200px;height:535px;
  background:linear-gradient(90deg,rgba(160,190,210,.35) 0%,rgba(120,160,200,.35) 35%,rgba(40,70,170,.45) 60%,rgba(180,190,200,.2) 80%,rgba(255,255,255,0) 100%);
  -webkit-mask:linear-gradient(180deg,#000 60%,transparent 100%);mask:linear-gradient(180deg,#000 60%,transparent 100%)}
.menu-icon{left:66px;top:90px;width:56px;height:24px}
.nav a{position:absolute;top:87px;color:var(--white);font-size:17px;text-decoration:none;letter-spacing:1.5px}
.nav-rule{top:98px;width:57px;height:1px;background:var(--ink)}
.brand{left:560px;top:60px;width:188px;text-align:center;font-weight:800;font-size:36px;line-height:36px;letter-spacing:3px;color:#b7bbc0}
.hero-rule{left:66px;top:219px;width:1068px;height:1px;background:rgba(255,255,255,.45)}
.hero-title{left:0;top:345px;width:1200px;text-align:center;font-size:30px;font-weight:600;color:#c5c8cc;letter-spacing:2px}
.hero-copy{left:0;top:405px;width:1200px;text-align:center;font-size:18px;line-height:30px;color:var(--white)}
.hero-btn{left:458px;top:500px;width:280px;height:77px;background:var(--button);color:var(--white);font-size:17px;display:flex;align-items:center;justify-content:center}

/* stats */
.section-title{left:0;top:848px;width:1200px;text-align:center;font-size:35px;font-weight:800;color:var(--muted);letter-spacing:4px}
.section-bar{left:560px;top:912px;width:78px;height:12px;background:var(--ink)}
.stat{top:967px;width:222px;height:222px;border-radius:50%;background:var(--ink);color:var(--white);display:flex;flex-direction:column;align-items:center;justify-content:center}
.stat b{font-size:33px;font-weight:800;line-height:34px;letter-spacing:3px}
.stat span{font-size:20px;font-weight:800;letter-spacing:3px}

/* doctors */
.doctor-frame{top:1342px;width:270px;height:270px;border:1px solid var(--line)}
.doctor-photo{top:1358px;width:271px;height:272px;background:linear-gradient(160deg,#c9c2b2 0%,#e9e6df 45%,#f1f1f1 70%,#3a3a44 100%)}
.doctor-name{top:1648px;font-size:25px;font-weight:300;letter-spacing:2px}
.doctor-role{top:1683px;font-size:17px;letter-spacing:1.5px}

/* products */
.product{left:66px;width:1068px;height:234px;border:1px solid var(--line)}
.product-photo{position:absolute;left:-1px;top:-1px;width:267px;height:234px}
.product h3{position:absolute;left:298px;top:40px;font-size:18px;font-weight:600;letter-spacing:1.5px}
.product p{position:absolute;left:298px;top:80px;width:650px;font-size:14px;line-height:23px;letter-spacing:.5px}
.product .cart{position:absolute;left:298px;top:156px;width:134px;height:40px;background:var(--button);color:var(--white);font-size:12px;display:flex;align-items:center;justify-content:center}
.see-more{left:0;top:2654px;width:1200px;text-align:center;font-size:15px;text-decoration:underline;letter-spacing:2px}

/* testimonial */
.quote-box{left:66px;top:2761px;width:1068px;height:378px;border:1px solid var(--line);border-bottom:none}
.quote-base{top:3138px;height:1px;background:var(--line)}
.quote-text{left:0;top:2904px;width:1200px;text-align:center;font-size:18px;line-height:30px}
.quote-name{left:0;top:3027px;width:1200px;text-align:center;font-size:15px}
.quote-photo{left:515px;top:3066px;width:146px;height:146px;border-radius:50%;background:radial-gradient(circle at 50% 40%,#c98a6a 0%,#b9573a 45%,#4a5e78 100%)}
.arrow{top:2935px;width:30px;height:30px}

/* footer */
.footer{left:0;top:3329px;width:1200px;height:449px;background:linear-gradient(180deg,#5b7fb3 0%,#3f5877 40%,var(--footer) 100%)}
.footer-col{top:3465px;color:var(--white)}
.footer-col h4{font-size:27px;font-weight:400;letter-spacing:2.5px;line-height:32px;margin-bottom:14px}
.footer-col li{list-style:none;font-size:15px;line-height:33.5px;letter-spacing:2px}
.news-input{left:929px;top:3546px;width:205px;height:42px;background:var(--white);color:var(--muted);font-size:10px;display:flex;align-items:center;justify-content:center}
.news-btn{left:929px;top:3603px;width:205px;height:44px;background:var(--button);color:var(--white);font-size:14px;letter-spacing:2px;display:flex;align-items:center;justify-content:center}
.social{top:3704px;width:14px;height:14px;border-radius:50%;background:var(--white)}
.footer-rule{left:66px;top:3731px;width:1068px;height:1px;background:rgba(255,255,255,.6)}
.copyright{left:0;top:3747px;width:1200px;text-align:center;color:var(--white);font-size:11px;letter-spacing:2px}
</style>
</head>
<body>

<div class="abs hero" role="img" aria-label="Laboratory test tubes with blue liquid"></div>
<div class="abs hero-tubes"></div>

<svg class="abs menu-icon" viewBox="0 0 56 24"><g stroke="#ffffff" stroke-width="1.5"><line x1="0" y1="2" x2="56" y2="2"/><line x1="0" y1="12" x2="56" y2="12"/><line x1="0" y1="22" x2="56" y2="22"/></g></svg>
<nav class="nav">
  <a style="left:214px">Home</a>
  <a style="left:355px">Doctors</a>
  <a style="left:883px">Services</a>
  <a style="left:1049px">About us</a>
</nav>
<div class="abs nav-rule" style="left:486px"></div>
<div class="abs nav-rule" style="left:772px"></div>
<div class="abs brand">QUIET<br>ORCHARD</div>
<div class="abs hero-rule"></div>
<h1 class="abs hero-title">Quiet Orchard</h1>
<p class="abs hero-copy">Lorem ipsum dolor sit amet, consectetur adipiscing elit. Morbi sed faci<br>lisis mauris. Praesent semper quam velit, sed aliquam urna sodales sit amet.</p>
<div class="abs hero-btn">Book Appointment</div>

<h2 class="abs section-title">DONE WORK</h2>
<div class="abs section-bar"></div>
<div class="abs stat" style="left:66px"><b>250+</b><span>CLINICS</span></div>
<div class="abs stat" style="left:348px"><b>250+</b><span>CLINICS</span></div>
<div class="abs stat" style="left:630px"><b>250+</b><span>CLINICS</span></div>
<div class="abs stat" style="left:911px"><b>250+</b><span>CLINICS</span></div>

<div class="abs doctor-frame" style="left:84px"></div>
<div class="abs doctor-photo" style="left:66px" role="img" aria-label="Doctor in white coat at his desk"></div>
<div class="abs doctor-name" style="left:66px">Owen</div>
<div class="abs doctor-role" style="left:66px">Dentist at Lorem</div>

<div class="abs doctor-frame" style="left:474px"></div>
<div class="abs doctor-photo" style="left:456px" role="img" aria-label="Doctor in white coat at his desk"></div>
<div class="abs doctor-name" style="left:456px">Owen</div>
<div class="abs doctor-role" style="left:456px">Dentist at Lorem</div>

<div class="abs doctor-frame" style="left:863px"></div>
<div class="abs doctor-photo" style="left:845px" role="img" aria-label="Doctor in white coat at his desk"></div>
<div class="abs doctor-name" style="left:845px">Owen</div>
<div class="abs doctor-role" style="left:845px">Dentist at Lorem</div>

<div class="abs product" style="top:1850px">
  <div class="product-photo" role="img" aria-label="Pile of white and coloured capsules" style="background:linear-gradient(135deg,#e8e4dc 0%,#d98a4a 35%,#f2f0ea 60%,#2f5a48 85%,#eeeae2 100%)"></div>
  <h3>Capsules</h3>
  <p>Lorem ipsum dolor sit amet, consectetur adipiscing elit, sed do eiusmod tempor incidi-dunt ut labore et dolore magna aliqua. Quis ipsum suspendisse.</p>
  <div class="cart">Add to cart</div>
</div>
<div class="abs product" style="top:2108px">
  <div class="product-photo" role="img" aria-label="Fish oil capsules spilling from a bottle" style="background:linear-gradient(135deg,#f6f4f0 0%,#e6a52a 40%,#d98410 60%,#f5f3ef 100%)"></div>
  <h3>Fish oil Capsules</h3>
  <p>Lorem ipsum dolor sit amet, consectetur adipiscing elit, sed do eiusmod tempor incidi-dunt ut labore et dolore magna aliqua. Quis ipsum suspendisse.</p>
  <div class="cart">Add to cart</div>
</div>
<div class="abs product" style="top:2368px">
  <div class="product-photo" role="img" aria-label="Eye dropper releasing a golden drop" style="background:linear-gradient(180deg,#e7ecec 0%,#dfe6e6 60%,#5fa898 85%,#1f8a78 100%)"></div>
  <h3>Eye droper</h3>
  <p>Lorem ipsum dolor sit amet, consectetur adipiscing elit, sed do eiusmod tempor incidi-dunt ut labore et dolore magna aliqua. Quis ipsum suspendisse.</p>
  <div class="cart">Add to cart</div>
</div>
<div class="abs see-more">SEE MORE</div>

<div class="abs quote-box"></div>
<div class="abs quote-base" style="left:66px;width:383px"></div>
<div class="abs quote-base" style="left:707px;width:427px"></div>
<svg class="abs arrow" style="left:117px" viewBox="0 0 30 30"><polyline points="20,3 8,15 20,27" fill="none" stroke="#333333" stroke-width="4"/></svg>
<svg class="abs arrow" style="left:1053px" viewBox="0 0 30 30"><polyline points="10,3 22,15 10,27" fill="none" stroke="#333333" stroke-width="4"/></svg>
<p class="abs quote-text">Lorem ipsum dolor sit amet, consectetur adipiscing elit. Morbi sed faci<br>lisis mauris. Praesent semper quam velit, sed aliquam urna sodales sit amet.<br>Aenean ultrices fringilla ipsum, at finibus eros</p>
<div class="abs quote-name">· Miles R.</div>
<div class="abs quote-photo" role="img" aria-label="Portrait of a smiling client"></div>

<div class="abs footer" role="img" aria-label="Glass office building under a blue sky"></div>
<div class="abs footer-col" style="left:66px"><h4>Our Services</h4><ul><li>Lorem</li><li>Ipsum</li><li>Dolor</li><li>Sit</li><li>Amet</li></ul></div>
<div class="abs footer-col" style="left:330px"><h4>Our Services</h4><ul><li>Lorem</li><li>Ipsum</li><li>Dolor</li><li>Sit</li><li>Amet</li></ul></div>
<div class="abs footer-col" style="left:594px"><h4>Our Services</h4><ul><li>Lorem</li><li>Ipsum</li><li>Dolor</li><li>Sit</li><li>Amet</li></ul></div>
<div class="abs footer-col" style="left:927px"><h4>Sign up for<br>our newsletter</h4></div>
<div class="abs news-input">Enter your email here</div>
<div class="abs news-btn">SIGN UP</div>
<div class="abs social" style="left:564px"></div>
<div class="abs social" style="left:592px"></div>
<div class="abs social" style="left:619px"></div>
<div class="abs footer-rule"></div>
<div class="abs copyright">All right reserved © Quiet Orchard 2021</div>

</body>
</html>
```